New Business Card Design Project

Updated business card design. I am moving towards more coaching of, for the most part women, who are searching for more in their lives. I am an intuitive healer, homeopath and nutritionist but also an author and motivational speaker. Int the past I have included my photo on the card but that is not essential. My book is called the Brilliance of Saffron - Reclaiming the Shade of Your Spirit so my colours are typically magenta.
Target Market(s)
Women - 35 - 60 considering improving their health. However, I am also a professional speaker with a target audience including corporate and conferences.
Industry/Entity Type
Health And Wellness
Contact Information for Business Card
Lucinda Parvell, Hom, RHN, BA
www.lucindaparvell.com
lucinda@lucindaparvell.com
519-362-7015
Facebook, instagram and twitter logos
Look and feel
Each slider illustrates characteristics of the customer's brand and the style your logo design should communicate.

```html
<!DOCTYPE html>
<html lang="en">
<head>
<meta charset="utf-8">
<title>Lucinda Parvell – Business Card</title>
<link href="https://fonts.googleapis.com/css2?family=Open+Sans:wght@400;600;700&display=swap" rel="stylesheet">
<style>
  :root{
    --magenta:#ec2d8c;
    --ink:#2b2b2b;
    --grey:#5a5a5a;
    --paper:#fafafa;
    --backdrop:#e9e6e1;
    --photo-top:#c9b79a;
    --photo-mid:#8a8f6a;
    --photo-low:#4f6a3c;
  }
  *{box-sizing:border-box;margin:0;padding:0}
  html,body{width:1200px;height:886px;overflow:hidden}
  body{background:var(--backdrop);font-family:"Open Sans",Arial,sans-serif;position:relative}
  .card{position:absolute;top:145px;width:340px;height:595px;background:var(--paper);
        box-shadow:0 6px 18px rgba(0,0,0,.18);overflow:hidden}
  .card--front{left:220px}
  .card--back{left:640px}

  /* front */
  .brand-mark{position:absolute;left:95px;top:150px;width:150px;height:150px;border-radius:50%;background:var(--magenta)}
  .rule{position:absolute;left:70px;top:330px;width:200px;height:2px;background:var(--ink)}
  .person-name{position:absolute;top:346px;width:100%;text-align:center;color:var(--magenta);
               font-weight:700;font-size:22px;letter-spacing:.3px}
  .credentials{position:absolute;top:378px;width:100%;text-align:center;color:var(--magenta);
               font-weight:600;font-size:13px}
  .contact{position:absolute;left:40px;top:440px;font-size:14px;line-height:24px;color:var(--grey)}
  .contact dt{display:inline;color:var(--magenta);font-weight:700}
  .contact dd{display:inline}
  .contact div{white-space:nowrap}

  /* back */
  .portrait{position:absolute;left:0;top:0;width:100%;height:440px;
            background:linear-gradient(160deg,var(--photo-top) 0%,#d8c8ad 35%,var(--photo-mid) 70%,var(--photo-low) 100%)}
  .signature-band{position:absolute;left:0;top:440px;width:100%;height:155px;background:#fff;text-align:center}
  .signature-name{margin-top:34px;font-size:30px;font-weight:400;color:var(--ink);letter-spacing:.5px}
  .tagline{margin-top:6px;font-size:13px;color:var(--grey);letter-spacing:.6px}
  .tagline span{color:var(--magenta);font-weight:700;padding:0 6px}
  .accent-line{display:block;margin:14px auto 0}
</style>
</head>
<body>
  <section class="card card--front" aria-label="Business card front">
    <div class="brand-mark" aria-hidden="true"></div>
    <div class="rule"></div>
    <h1 class="person-name">Lucinda Parvell</h1>
    <p class="credentials">Hom, RHN, BA</p>
    <dl class="contact">
      <div><dt>Phone:</dt> <dd>519-362-7015</dd></div>
      <div><dt>Email:</dt> <dd>lucinda@lucindaparvell.com</dd></div>
      <div><dt>Web:</dt> <dd>www.lucindaparvell.com</dd></div>
    </dl>
  </section>

  <section class="card card--back" aria-label="Business card back">
    <div class="portrait" role="img" aria-label="Photo of Lucinda Parvell in a white top leaning against a brick wall beside green leaves"></div>
    <div class="signature-band">
      <p class="signature-name">Lucinda Parvell</p>
      <p class="tagline"><span>•</span>wellness renegade<span>•</span></p>
      <svg class="accent-line" width="200" height="4" viewBox="0 0 200 4" aria-hidden="true">
        <path d="M0 2 Q100 0 200 2" stroke="#ec2d8c" stroke-width="1.5" fill="none"/>
      </svg>
    </div>
  </section>
</body>
</html>
```